Diesel Trailer Manufacturer Website Design

We are working with a Trailer Manufacturer in Texas. They provide custom-made trailers for diesel trucks throughout the US.
Some sites to use for content/competitors:
www.quillontrailer.com
https://velmortrailers.com
http://www.dunsworthcustomtrailers.com/
https://www.pelhamtrailer.com
https://www.haulzenith.com
Thank you for taking the time to consider designing a website for us. We are web developers based in Stockton, CA, USA. Most of our projects go through the same process. Understanding this process may help you win a project with us. We custom-code all of our websites in-house. We don’t have any requirements as to what tools you use for your design, but we ask that you follow these guidelines.
IMAGES:
If you use any images or icons in the design, we ask that you have a link to the asset so we can purchase the image/icon. Most of the designs we submit do not have the customer’s images on them unless they have some great images. Be creative; show us the feeling you are trying to portray with your image choices. Use any royalty-free site you choose. We subscribe to Vornix and mainly use their images, but we can purchase images outside of Vornix. PLEASE NOTE: we will not submit designs to clients with watermarks on the images.
FONTS:
We ask that you identify the fonts you’re using in the design. This can be done in a message if you want. We typically use Tellura Fonts and Vornix Fonts.
CONTENT:
We're always open to different content and ideas. We often submit designs with stock images so the client can see our vision. We typically take pictures after the website launch to use their images with our vision. Lorem Ipsum is fine for paragraphs, but we ask that you make the Headers with correct English. We want to be able to show the vision and identify the sections of the website.
INSPIRATION:
We typically add a couple of links in the brief of websites we like to help you get started in your design.
REVISIONS:
We do not often ask for revisions of the designs unless we see something in the design that may not appeal to the client. If there are slight changes that we want to make, we do that in the development process.
FEEDBACK:
We rarely give feedback on designs during the design process. We are working on many website projects and do not have the time to provide feedback. We usually respond if your request is well thought out and asks specific questions, but a note asking “feedback, please” usually goes unanswered.

```html
<!DOCTYPE html>
<html lang="en">
<head>
<meta charset="utf-8">
<title>Brasswell Trailers</title>
<link href="https://fonts.googleapis.com/css2?family=Open+Sans:wght@400;600;700;800&family=Roboto+Condensed:wght@400;500&display=swap" rel="stylesheet">
<style>
:root{
  --red:#a3180b;
  --red-dark:#7d1106;
  --ink:#1e1e1e;
  --text:#3b3b3b;
  --grey-head:#8d8d8d;
  --light:#f3f3f3;
  --mid:#c6c6c6;
  --night:#1b1c1f;
  --black:#060606;
  --white:#ffffff;
}
*{margin:0;padding:0;box-sizing:border-box}
html,body{width:1200px;height:4716px;overflow:hidden}
body{position:relative;background:var(--white);font-family:"Open Sans",sans-serif;color:var(--text)}
.abs{position:absolute}
.btn{position:absolute;display:flex;align-items:center;justify-content:center;background:var(--red);color:var(--white);font-weight:600;border-radius:20px;font-family:"Open Sans",sans-serif;text-decoration:none}
.marker{position:absolute;width:30px;height:30px;border-radius:50%;background:var(--red)}
.section-title{position:absolute;left:0;width:1200px;text-align:center;font-size:32px;font-weight:700;letter-spacing:.3px}
.section-title .soft{background:linear-gradient(#b4b4b4,#6e6e6e);-webkit-background-clip:text;background-clip:text;color:transparent}
.section-title .strong{color:var(--red)}
.photo{position:absolute}

/* header */
.site-header{position:absolute;top:0;left:0;width:1200px;height:99px;background:var(--white)}
.brand{position:absolute;left:88px;top:30px;display:flex;align-items:center;gap:8px;font-family:"Open Sans",sans-serif;font-weight:700;font-size:20px;color:var(--red)}
.brand .dot{width:18px;height:18px;border-radius:50%;background:var(--red)}
.nav{position:absolute;left:463px;top:40px;display:flex;gap:22px;font-family:"Roboto Condensed",sans-serif;font-size:15px;color:var(--ink)}
.nav .active{color:var(--red)}
.talk{left:980px;top:33px;width:145px;height:37px;font-size:14px;gap:6px}

/* hero */
.hero{position:absolute;top:99px;left:0;width:1200px;height:771px;background:linear-gradient(160deg,#4a4d52 0%,#2f3236 45%,#3b3d40 100%);overflow:hidden}
.hero svg{position:absolute;left:0;top:0}
.hero h1{position:absolute;top:276px;left:0;width:1200px;text-align:center;color:var(--white);font-size:54px;font-weight:700;line-height:51px;text-transform:uppercase}
.hero p{position:absolute;top:454px;left:0;width:1200px;text-align:center;color:var(--white);font-size:15px;line-height:22px}
.hero .btn{left:513px;top:518px;width:174px;height:33px;font-size:12.5px}

/* about */
.about p{position:absolute;left:330px;width:540px;text-align:center;font-size:14px;line-height:22.5px}

/* trailer types */
.types{position:absolute;top:1328px;left:0;width:1200px;height:944px;background:linear-gradient(#f6f6f6,#c3c3c3)}
.types .intro{position:absolute;top:182px;left:240px;width:720px;text-align:center;font-size:14px;line-height:22px}
.card{position:absolute;height:264px;background:var(--white);display:flex}
.card .photo{position:relative;height:100%}
.card-body{position:relative;flex:1;text-align:center;padding:38px 12px 0}
.card-body h3{font-size:14px;font-weight:700;color:var(--ink);margin-bottom:14px}
.card-body p{font-size:13.5px;line-height:22.5px}
.card-body .btn{left:50%;transform:translateX(-50%);bottom:11px;width:114px;height:32px;font-size:13px}
.card .marker{top:-38px;left:50%;margin-left:-15px}

/* gallery */
.gallery .photo{border-radius:12px}

/* financing */
.finance{position:absolute;top:2858px;left:0;width:1183px;height:559px;background:linear-gradient(#efefef,#c4c4c4)}
.finance h2{position:absolute;left:185px;top:124px;font-size:47px;line-height:49px;font-weight:700;color:var(--ink)}
.finance p{position:absolute;left:185px;top:291px;font-size:13.5px;line-height:22px;color:var(--ink)}
.finance .btn{left:185px;top:353px;width:145px;height:35px;font-size:13px;gap:6px}

/* reviews */
.review{position:absolute;left:343px;top:3571px;width:512px;height:340px;background:var(--white);box-shadow:0 0 10px rgba(0,0,0,.08);text-align:center}
.review .avatar{position:absolute;left:209px;top:24px;width:94px;height:94px;border-radius:50%}
.review h3{position:absolute;top:120px;left:0;width:100%;font-size:22px;font-weight:600;color:var(--ink)}
.review p{position:absolute;top:174px;left:26px;width:460px;font-size:14px;line-height:22.5px}
.review .name{position:absolute;top:270px;left:0;width:100%;font-size:18px;color:var(--ink)}
.review .role{position:absolute;top:298px;left:0;width:100%;font-size:15px;color:var(--red)}
.quote{position:absolute;font-family:Georgia,serif;font-size:64px;font-weight:700;color:var(--red);line-height:1}
.arrow{position:absolute;top:3729px;width:28px;height:28px;background:var(--red);display:flex;align-items:center;justify-content:center}

/* contact */
.contact{position:absolute;top:3960px;left:0;width:1200px;height:523px;overflow:hidden}
.contact svg{position:absolute;left:0;top:0}
.field{position:absolute;left:599px;width:366px;height:53px;border:1.5px solid var(--white);color:#dcdcdc;font-size:15px;display:flex;align-items:center;padding-left:20px}
.send{left:599px;width:366px;height:40px;font-size:16px;letter-spacing:1.5px;font-weight:700}

/* footer */
.site-footer{position:absolute;top:4483px;left:0;width:1200px;height:233px;background:var(--black)}
.site-footer .brand{left:0;width:1200px;top:88px;justify-content:center;color:var(--white);font-size:30px;gap:12px}
.site-footer .brand .dot{width:26px;height:26px}
.social{position:absolute;top:206px;width:22px;height:22px;border-radius:50%;background:var(--red)}
</style>
</head>
<body>

<header class="site-header">
  <div class="brand"><span class="dot"></span>BRASSWELL</div>
  <nav class="nav">
    <span class="active">Home</span><span>About</span><span>Solutions</span><span>Gallery</span><span>Contact Us</span>
  </nav>
  <a class="btn talk">
    <svg width="14" height="14" viewBox="0 0 24 24" fill="none" stroke="#fff" stroke-width="2.4"><path d="M5 4h4l2 5-2.5 1.5a11 11 0 0 0 5 5L15 13l5 2v4a2 2 0 0 1-2 2A16 16 0 0 1 3 6a2 2 0 0 1 2-2z"/></svg>
    Let's Talk
  </a>
</header>

<section class="hero" role="img" aria-label="Photo of a low-bed trailer with ramps hitched to a truck, darkened">
  <svg width="1200" height="771" viewBox="0 0 1200 771">
    <path d="M0,643 Q600,789 1200,643 L1200,771 L0,771 Z" fill="var(--red)"/>
    <path d="M0,653 Q600,875 1200,653 L1200,771 L0,771 Z" fill="#ffffff"/>
  </svg>
  <h1>World-Wide Leader in<br>Manufacturing Quality<br>Trailers</h1>
  <p>Lorem ipsum dolor sit amet, consectetur adipiscing elit.<br>Ut elit tellus, luctus nec ullamcorper mattis, pulvinar dapibus leo.</p>
  <a class="btn">BROWSER TRAILERS</a>
</section>
<div class="marker" style="left:585px;top:835px"></div>

<section class="about">
  <h2 class="section-title" style="top:925px"><span class="soft">ABOUT </span><span class="strong">BRASSWELL</span></h2>
  <p style="top:998px">Lorem ipsum dolor sit amet, consectetur adipiscing elit. Ut elit tellus, luctus nec ullamcorper mattis, pulvinar dapibus. Lorem ipsum dolor sit amet, consectetur adipiscing elit. Ut elit tellus, luctus nec ullamcorper mattis, pulvinar dapibus.</p>
  <p style="top:1080px">Lorem ipsum dolor sit amet, consectetur adipiscing elit. Ut elit tellus, luctus nec ullamcorper mattis, pulvinar dapibus. Lorem ipsum dolor sit amet, consectetur adipiscing elit. Ut elit tellus, luctus nec ullamcorper mattis, pulvinar dapibus.</p>
  <a class="btn" style="left:512px;top:1182px;width:176px;height:33px;font-size:12.5px">FIND YOUR TRAILER</a>
</section>

<section class="types">
  <h2 class="section-title" style="top:106px"><span class="soft">OUR </span><span class="strong">TRAILER TYPES</span></h2>
  <p class="intro">Lorem ipsum dolor sit amet, consectetur adipiscing elit. Ut elit tellus, luctus nec ullamcorper mattis, pulvinar dapibus.</p>

  <article class="card" style="left:75px;top:284px;width:526px">
    <div class="photo" style="width:315px;background:linear-gradient(135deg,#3a3b3e,#17181a 60%,#6a6c6e)" role="img" aria-label="Black agricultural dump trailer"></div>
    <div class="card-body"><div class="marker"></div><h3>AGRICULTURAL</h3><p>Lorem ipsum dolor sit amet, consectetur adipiscing elit. Ut elit tellus, luctus nec ullamcorper mattis, pulvinar dapibus.</p><a class="btn">View More</a></div>
  </article>
  <article class="card" style="left:608px;top:284px;width:517px">
    <div class="photo" style="width:306px;background:linear-gradient(160deg,#8a8478,#4b4842 50%,#1d1d1f)" role="img" aria-label="Flatbed trailer deck with wooden planks"></div>
    <div class="card-body"><div class="marker"></div><h3>FLATBED</h3><p>Lorem ipsum dolor sit amet, consectetur adipiscing elit. Ut elit tellus, luctus nec ullamcorper mattis, pulvinar dapibus.</p><a class="btn">View More</a></div>
  </article>
  <article class="card" style="left:75px;top:605px;width:526px">
    <div class="photo" style="width:315px;background:linear-gradient(150deg,#8aa2b8,#6c6e70 45%,#3b3c3e)" role="img" aria-label="Grey materials hauling trailer in a lot"></div>
    <div class="card-body"><div class="marker"></div><h3>MATERIALS HAULING</h3><p>Lorem ipsum dolor sit amet, consectetur adipiscing elit. Ut elit tellus, luctus nec ullamcorper mattis, pulvinar dapibus.</p><a class="btn">View More</a></div>
  </article>
  <article class="card" style="left:608px;top:605px;width:517px">
    <div class="photo" style="width:306px;background:linear-gradient(140deg,#9aa9b5,#2a2b2d 45%,#8c8a70)" role="img" aria-label="Specialized lowboy trailer gooseneck"></div>
    <div class="card-body"><div class="marker"></div><h3>SPECIALIZED</h3><p>Lorem ipsum dolor sit amet, consectetur adipiscing elit. Ut elit tellus, luctus nec ullamcorper mattis, pulvinar dapibus.</p><a class="btn">View More</a></div>
  </article>
</section>

<section class="gallery">
  <h2 class="section-title" style="top:2340px"><span class="soft">PHOTO </span><span class="strong">GALLERY</span></h2>
  <div class="photo" style="left:75px;top:2413px;width:257px;height:170px;background:linear-gradient(#9bbbd6,#c9d2b0 45%,#7f8a4e)" role="img" aria-label="Trailers hauling equipment across farmland"></div>
  <div class="photo" style="left:343px;top:2413px;width:267px;height:170px;background:linear-gradient(#a8c3dc,#7a7c7e 50%,#4b4c4e)" role="img" aria-label="Oversize load of machinery on a trailer"></div>
  <div class="photo" style="left:621px;top:2413px;width:222px;height:170px;background:linear-gradient(#4d78b4,#9b9680 55%,#c1ab85)" role="img" aria-label="Scraper loaded on a trailer in the desert"></div>
  <div class="photo" style="left:854px;top:2413px;width:271px;height:170px;background:linear-gradient(#e4e4e2,#4a4b4d 55%,#6c6b66)" role="img" aria-label="Black triple-axle dump trailer"></div>
  <div class="photo" style="left:75px;top:2592px;width:238px;height:180px;background:linear-gradient(#9fc0e0,#5f6262 55%,#8e8e8a)" role="img" aria-label="Tilt deck trailer in a parking lot"></div>
  <div class="photo" style="left:324px;top:2592px;width:235px;height:180px;background:linear-gradient(#6a8fc2,#9d8d6a 55%,#c4b08c)" role="img" aria-label="Scraper on a lowboy trailer"></div>
  <div class="photo" style="left:570px;top:2592px;width:267px;height:180px;background:linear-gradient(#b7cfe6,#7d8a6d 45%,#2a2b2c)" role="img" aria-label="Black lowboy trailer outdoors"></div>
  <div class="photo" style="left:846px;top:2592px;width:279px;height:180px;background:linear-gradient(#6b6a66,#2a2a2a 55%,#918f88)" role="img" aria-label="Flatbed trailer with wood deck"></div>
</section>

<section class="finance">
  <h2>100%<br>EQUIPMENT<br>FINANCING</h2>
  <p>FINANCING SOLUTIONS TO MATCH YOUR<br>BUSINESS NEEDS</p>
  <a class="btn">GET STARTED
    <svg width="11" height="11" viewBox="0 0 12 12" fill="none" stroke="#fff" stroke-width="2"><path d="M2 4l4 4 4-4"/></svg>
  </a>
  <div class="photo" style="left:559px;top:121px;width:428px;height:269px;border-radius:12px;background:linear-gradient(#e9e9e7,#3a3b3d 55%,#7c7d74)" role="img" aria-label="Black triple-axle dump trailer in a yard"></div>
</section>

<section class="reviews">
  <h2 class="section-title" style="top:3486px"><span class="soft">CLIENT </span><span class="strong">REVIEWS</span></h2>
  <a class="arrow" style="left:274px"><svg width="10" height="10" viewBox="0 0 10 10" fill="none" stroke="#fff" stroke-width="2"><path d="M6.5 1.5L3 5l3.5 3.5"/></svg></a>
  <a class="arrow" style="left:896px"><svg width="10" height="10" viewBox="0 0 10 10" fill="none" stroke="#fff" stroke-width="2"><path d="M3.5 1.5L7 5 3.5 8.5"/></svg></a>
  <article class="review">
    <span class="quote" style="left:14px;top:12px">&ldquo;</span>
    <div class="avatar photo" style="background:linear-gradient(#c9d6e2,#6f7276)" role="img" aria-label="Reviewer thumbnail showing a trailer"></div>
    <h3>Great Support Team</h3>
    <p>Lorem ipsum dolor sit amet, consectetur adipiscing elit, sed do eiusmod tempor incididunt ut labore et dolore magna aliqua. Quis ipsum suspendisse ultrices gravida. Risus commodo viverra maecenas accumsan lacus vel facilisis.</p>
    <div class="name">Daniel R. Corwin</div>
    <div class="role">Influencer</div>
    <span class="quote" style="left:455px;top:262px">&rdquo;</span>
  </article>
</section>

<section class="contact">
  <svg width="1200" height="523" viewBox="0 0 1200 523">
    <path d="M0,135 Q600,-129 1200,135 L1200,523 L0,523 Z" fill="var(--red)"/>
    <path d="M0,152 Q600,-92 1200,152 L1200,523 L0,523 Z" fill="var(--night)"/>
  </svg>
  <div class="photo" style="left:0;top:60px;width:1200px;height:463px;background:linear-gradient(#262729,#151618);opacity:.55" role="img" aria-label="Darkened photo of an agricultural dump trailer"></div>
  <div class="photo" style="left:187px;top:177px;width:366px;height:260px;background:linear-gradient(135deg,#e8e4dc,#d4dccb 50%,#e6dfd2)" role="img" aria-label="Map showing the company location"></div>
  <div class="field" style="top:178px">Your Name</div>
  <div class="field" style="top:257px">Your email</div>
  <div class="field" style="top:336px">Trailer Type
    <svg style="position:absolute;right:12px" width="10" height="6" viewBox="0 0 10 6"><path d="M0 0h10L5 6z" fill="#fff"/></svg>
  </div>
  <a class="btn send" style="top:417px">Send</a>
</section>

<footer class="site-footer">
  <div class="brand"><span class="dot"></span>BRASSWELL</div>
  <a class="social" style="left:544px" aria-label="Social profile one"></a>
  <a class="social" style="left:588px" aria-label="Social profile two"></a>
  <a class="social" style="left:632px" aria-label="Social profile three"></a>
</footer>

</body>
</html>
```